Webdesign for jewellery manufacturer.

Design is for the jewellery manufacturer for Polish company.
Language versions: en, de
Logo like on v_e_l_m_o_r*pl
Menu items:
- about us (static page)
- offer
- wholesale orders (static page)
- special orders (portfolio page: image + description
- finished products (product list page → product detail page)
- contact
- news (blog list → blog page)
Page items
- menu
- social links (FB, instagram)
- content
- footer
- language links
Home page items
- banner
- about us introduction
- offer sections: wholesale orders, special orders, finished products
- latest news
Final design must be coded to in html copatibile to this theme framework https://brindlecms.example/theme/tovaro-quillkit
All page types must be coded: homepage, static content page, product list/portfolio list page, blog list page/blog content page
You can use attached images or any images posed on instagram linked on homepage above.
Jewellery sellers

```html
<!DOCTYPE html>
<html lang="en">
<head>
<meta charset="utf-8">
<title>Velmor — Jewellery</title>
<link href="https://fonts.googleapis.com/css2?family=Montserrat:wght@400;500;600;700&display=swap" rel="stylesheet">
<style>
:root{
  --accent:#d6a676;
  --accent-dark:#c58f5c;
  --ink:#1d1b1c;
  --text:#333;
  --muted:#777;
  --light:#f4f3f3;
  --dark:#1b191c;
  --line:#e3e3e3;
}
*{box-sizing:border-box;margin:0;padding:0}
html,body{width:1200px;height:4545px;overflow:hidden}
body{position:relative;font-family:'Montserrat',sans-serif;color:var(--text);background:#fff}
.abs{position:absolute}
a{color:inherit;text-decoration:none}

.topbar{left:0;top:0;width:1200px;height:35px;background:var(--dark);color:#fff;font-size:15px;font-style:italic;text-align:center;line-height:35px}
.topbar .close{position:absolute;right:20px;top:0;font-style:normal;font-weight:700}

.header{left:0;top:35px;width:1200px;height:89px;background:#fff}
.logo{left:104px;top:26px;font-family:'Montserrat',sans-serif;font-size:30px;font-weight:500;color:var(--accent);line-height:36px}
.search{left:415px;top:22px;width:405px;height:48px;border:1px solid #cfcfcf;border-radius:24px;font-size:14px;line-height:46px;padding-left:18px;color:#555}
.search .btn{position:absolute;right:4px;top:4px;width:40px;height:40px;border-radius:50%;background:var(--accent)}
.lang{left:866px;top:36px;font-size:13px}
.icons{left:922px;top:32px;display:flex;gap:30px}
.icons svg{width:24px;height:24px;stroke:var(--ink);fill:none;stroke-width:1.8}

.nav{left:0;top:124px;width:1200px;height:45px;background:var(--accent);display:flex;gap:30px;padding-left:112px;font-size:14px;color:#fff;line-height:45px}
.nav .active{color:var(--ink)}

.hero{left:0;top:169px;width:1200px;height:532px;background:linear-gradient(90deg,#565152 0%,#625c5e 55%,#7a6f6c 100%)}
.hero .photo{position:absolute;right:0;top:0;width:560px;height:532px;background:radial-gradient(ellipse at 65% 45%,#c79a83 0%,#8c6f66 45%,rgba(110,100,100,0) 75%)}
.hero h1{position:absolute;left:86px;top:150px;font-size:66px;font-weight:600;color:#fff;letter-spacing:2px}
.hero p{position:absolute;left:90px;top:228px;width:640px;font-size:20px;line-height:30px;color:#fff}
.btn-pill{display:inline-block;background:var(--accent);color:#fff;border-radius:30px;font-weight:600;text-align:center}
.hero .btn-pill{position:absolute;left:91px;top:318px;width:174px;height:46px;line-height:46px;font-size:19px}

.section-title{left:0;width:1200px;text-align:center;font-size:40px;font-weight:600;letter-spacing:7px;color:var(--ink)}
.tabs{left:295px;top:852px;display:flex;gap:12px}
.tabs span{background:#e8e8e8;height:43px;line-height:43px;font-size:15px;text-align:center;color:#333}

.row{left:90px;width:1020px;display:flex;gap:21px}
.card{width:240px;text-align:center}
.card .pic{position:relative;width:240px;height:298px}
.badge{position:absolute;top:8px;height:30px;line-height:30px;padding:0 14px;background:var(--accent-dark);color:#fff;font-size:16px}
.badge.left{left:-4px}
.badge.right{right:-4px}
.card .name{margin-top:15px;font-size:15px;line-height:21px;color:#222}
.card .price{margin-top:8px;font-size:16px;color:#111}
.arrow{width:14px;height:24px;stroke:#333;fill:none;stroke-width:2}

.about{left:0;top:1408px;width:1200px;height:507px;background:linear-gradient(90deg,#806a62 0%,#4a3c3c 35%,#2e2428 60%,#2b2327 100%)}
.about .photo{position:absolute;left:0;top:0;width:560px;height:507px;background:radial-gradient(ellipse at 40% 45%,#c59a80 0%,#7d5f58 50%,rgba(50,40,42,0) 85%)}
.about h2{position:absolute;left:651px;top:126px;font-size:40px;font-weight:600;letter-spacing:6px;color:#fff}
.about p{position:absolute;left:651px;top:196px;width:465px;font-size:14px;line-height:29.5px;color:#fff}
.about .btn-pill{position:absolute;left:652px;top:330px;width:142px;height:44px;line-height:44px;font-size:15px}

.news-bg{left:0;top:3106px;width:1200px;height:680px;background:var(--light)}
.news-card{position:absolute;top:3268px;width:330px;height:417px;background:#fff;border:1px solid var(--line);padding:5px}
.news-card .pic{height:198px;position:relative}
.news-card .date{position:absolute;left:16px;bottom:-20px;width:62px;height:62px;background:var(--accent);color:#fff;text-align:center;font-size:20px;line-height:25px;padding-top:6px}
.news-card h3{margin:42px 0 0 14px;font-size:17px;font-weight:500;line-height:25px;color:#222}
.news-card p{margin:12px 14px 0;font-size:13px;line-height:24px;color:#777}
.news-card .more{display:block;margin:10px 14px 0;font-size:13px;font-weight:700;color:var(--accent-dark)}

.newsletter p{position:absolute;left:160px;top:3955px;width:880px;text-align:center;font-size:16px;line-height:27px;color:#333}
.subscribe{left:250px;top:4017px;width:700px;height:60px;border:1px solid #ddd;border-radius:30px;font-size:14px;line-height:58px;padding-left:34px;color:#888}
.subscribe .btn-pill{position:absolute;right:4px;top:4px;width:170px;height:50px;line-height:50px;font-size:18px}

.footer{left:0;top:4177px;width:1200px;height:368px;background:var(--dark);color:#fff}
.footer h4{position:absolute;top:72px;font-size:21px;font-weight:500}
.footer .links{position:absolute;top:122px;font-size:12px;line-height:24.5px}
.footer .field{position:absolute;left:826px;top:127px;width:284px;height:42px;border:1px solid #ccc;font-size:11px;line-height:40px;padding-left:20px}
.footer .signup{position:absolute;left:826px;top:188px;width:284px;height:42px;background:var(--accent);text-align:center;line-height:42px;font-size:16px;font-weight:600}
.footer .copy{position:absolute;left:90px;top:334px;font-size:11px}
.cards{position:absolute;left:942px;top:326px;display:flex;gap:6px}
.cards span{width:40px;height:24px;background:#e6e6e6}
.cards span:nth-child(2){background:#e8a33c}
.cards span:nth-child(3){background:#4a6fb5}
.cards span:nth-child(4){background:#9cc2e6}
</style>
</head>
<body>

<div class="abs topbar">Free shipping worldwide on all orders over $200<span class="close">✕</span></div>

<header class="abs header">
  <div class="abs logo">Velmor</div>
  <div class="abs search">Search Items<span class="btn"></span></div>
  <div class="abs lang">En ▾</div>
  <div class="abs icons">
    <svg viewBox="0 0 24 24"><path d="M12 20l-7-7a4.5 4.5 0 016.4-6.4L12 7l.6-.4A4.5 4.5 0 0119 13z"/></svg>
    <svg viewBox="0 0 24 24"><path d="M5 8h14l-1 13H6zM9 8V6a3 3 0 016 0v2"/></svg>
    <svg viewBox="0 0 24 24"><circle cx="12" cy="8" r="4"/><path d="M4 21c1-5 15-5 16 0"/></svg>
    <svg viewBox="0 0 24 24"><rect x="3" y="5" width="18" height="14" rx="2"/><path d="M3 7l9 6 9-6"/></svg>
  </div>
</header>

<nav class="abs nav">
  <span class="active">Jewellery ▾</span><span>Diamonds ▾</span><span>Engagement ▾</span><span>Wedding ▾</span><span>Watches Sale ▾</span><span>Fashion Jewelry ▾</span><span>Communion Baptism ▾</span><span>Blog</span>
</nav>

<section class="abs hero">
  <div class="photo" role="img" aria-label="Woman wearing a gold necklace and earrings"></div>
  <h1>VELMOR</h1>
  <p>Lorem ipsum dolor sit amet, consectetur adipiscing elit, sed do eiusmod tempor incididunt ut</p>
  <a class="btn-pill">Buy Now</a>
</section>

<h2 class="abs section-title" style="top:790px">WHOLESALE ORDERS</h2>
<div class="abs tabs"><span style="width:155px">News</span><span style="width:234px">Most frequently bought</span><span style="width:195px">Sale</span></div>

<svg class="abs arrow" style="left:39px;top:1064px" viewBox="0 0 14 24"><path d="M10 4L3 12l7 8"/></svg>
<svg class="abs arrow" style="left:1147px;top:1064px" viewBox="0 0 14 24"><path d="M4 4l7 8-7 8"/></svg>
<div class="abs row" style="top:927px">
  <div class="card"><div class="pic" role="img" aria-label="Model wearing a bracelet with pearls" style="background:linear-gradient(160deg,#5d6a3d,#8a6a55 50%,#c49a80)"><span class="badge left">New</span></div><div class="name">Bracelet with a chain<br>of pearls</div><div class="price">PLN 77</div></div>
  <div class="card"><div class="pic" role="img" aria-label="Model wearing a long chain necklace" style="background:linear-gradient(160deg,#4e5a3a,#8a7462 50%,#c9a992)"><span class="badge left">New</span></div><div class="name">Long chain necklace<br>with pearls</div><div class="price">PLN 323</div></div>
  <div class="card"><div class="pic" role="img" aria-label="Model wearing a delicate gold ring set" style="background:linear-gradient(160deg,#4f5c3b,#9a7b68 50%,#d0ae98)"><span class="badge right">Sale</span></div><div class="name">Delicate gold set.<br>ring ...</div><div class="price">PLN 2 034</div></div>
  <div class="card"><div class="pic" role="img" aria-label="Model wearing gilded navy blue earrings" style="background:linear-gradient(160deg,#56643f,#927563 50%,#cba894)"></div><div class="name">Lumera gilded navy<br>blue earrings</div><div class="price">545 PLN</div></div>
</div>

<section class="abs about">
  <div class="photo" role="img" aria-label="Portrait of a model wearing rings and a bracelet"></div>
  <h2>ABOUT US</h2>
  <p>Lorem ipsum dolor sit amet, consectetur adipiscing elit, sed do eiusmod tempor incididunt ut labore et dolore magna aliqua. Ut enim ad minim veniam, quis nostrud exercitation ullamco laboris nisi ut aliquip ex ea commodo consequat.</p>
  <a class="btn-pill">Read More</a>
</section>

<h2 class="abs section-title" style="top:2006px">SPECIAL ORDERS</h2>
<svg class="abs arrow" style="left:39px;top:2216px" viewBox="0 0 14 24"><path d="M10 4L3 12l7 8"/></svg>
<svg class="abs arrow" style="left:1147px;top:2216px" viewBox="0 0 14 24"><path d="M4 4l7 8-7 8"/></svg>
<div class="abs row" style="top:2079px">
  <div class="card"><div class="pic" role="img" aria-label="Gold and silver heart pendant" style="background:radial-gradient(circle at 50% 45%,#e5cf8a,#efefef 60%)"><span class="badge left">New</span></div><div class="name">Bracelet with a chain<br>of pearls</div><div class="price">PLN 77</div></div>
  <div class="card"><div class="pic" role="img" aria-label="Gold crown with a ruby cross" style="background:radial-gradient(circle at 50% 55%,#d9b45a,#f3f3f3 62%)"><span class="badge left">New</span></div><div class="name">Long chain necklace<br>with pearls</div><div class="price">PLN 323</div></div>
  <div class="card"><div class="pic" role="img" aria-label="Purple stone ring with diamonds" style="background:radial-gradient(circle at 50% 45%,#7a6cc2,#d8d8e0 45%,#efefef 65%)"><span class="badge right">Sale</span></div><div class="name">Delicate gold set.<br>ring ...</div><div class="price">PLN 2 034</div></div>
  <div class="card"><div class="pic" role="img" aria-label="Purple stone ring in silver setting" style="background:radial-gradient(circle at 50% 40%,#6c5fc0,#d8d8e0 42%,#efefef 62%)"></div><div class="name">Lumera gilded navy<br>blue earrings</div><div class="price">545 PLN</div></div>
</div>

<h2 class="abs section-title" style="top:2552px">FINISHED PRODUCTS</h2>
<svg class="abs arrow" style="left:39px;top:2762px" viewBox="0 0 14 24"><path d="M10 4L3 12l7 8"/></svg>
<svg class="abs arrow" style="left:1147px;top:2762px" viewBox="0 0 14 24"><path d="M4 4l7 8-7 8"/></svg>
<div class="abs row" style="top:2624px">
  <div class="card"><div class="pic" role="img" aria-label="Gold family pendant necklace" style="background:radial-gradient(circle at 50% 60%,#d9bd74,#f0efee 55%)"><span class="badge left">New</span></div><div class="name">Bracelet with a chain<br>of pearls</div><div class="price">PLN 77</div></div>
  <div class="card"><div class="pic" role="img" aria-label="Gold ring with amber stone" style="background:radial-gradient(circle at 50% 50%,#d98a2a,#e2c36a 25%,#f0efee 55%)"><span class="badge left">New</span></div><div class="name">Long chain necklace<br>with pearls</div><div class="price">PLN 323</div></div>
  <div class="card"><div class="pic" role="img" aria-label="Model wearing layered gold chains" style="background:linear-gradient(180deg,#b98a72,#d6b39a 55%,#c9a48c)"><span class="badge right">Sale</span></div><div class="name">Delicate gold set.<br>ring ...</div><div class="price">PLN 2 034</div></div>
  <div class="card"><div class="pic" role="img" aria-label="Jeweller working at a bench" style="background:linear-gradient(160deg,#9b9a95,#4f4e4f 50%,#2d2c30)"></div><div class="name">Lumera gilded navy<br>blue earrings</div><div class="price">545 PLN</div></div>
</div>

<div class="abs news-bg"></div>
<h2 class="abs section-title" style="top:3197px">LATEST NEWS</h2>
<article class="news-card" style="left:90px"><div class="pic" role="img" aria-label="Woman wearing a gold pendant" style="background:linear-gradient(160deg,#f1ede8,#d9b49a 55%,#b68a6c)"><div class="date">25<br>FEB</div></div><h3>Lorem ipsum dolor sit amet,<br>consectetur adipiscing</h3><p>Lorem ipsum dolor sit amet, consect etur adipiscing elit, sed do eiusmtempor incididunt ut labore et dolore</p><a class="more">READ MORE</a></article>
<article class="news-card" style="left:436px"><div class="pic" role="img" aria-label="Hand wearing an emerald ring" style="background:linear-gradient(160deg,#3c5a2e,#b58a74 55%,#d9aea0)"><div class="date">25<br>FEB</div></div><h3>Lorem ipsum dolor sit amet,<br>consectetur adipiscing</h3><p>Lorem ipsum dolor sit amet, consect etur adipiscing elit, sed do eiusmtempor incididunt ut labore et dolore</p><a class="more">READ MORE</a></article>
<article class="news-card" style="left:778px"><div class="pic" role="img" aria-label="Hand wearing a ring by green leaves" style="background:linear-gradient(160deg,#4a3a30,#c29a86 50%,#6e7a3a)"><div class="date">25<br>FEB</div></div><h3>Lorem ipsum dolor sit amet,<br>consectetur adipiscing</h3><p>Lorem ipsum dolor sit amet, consect etur adipiscing elit, sed do eiusmtempor incididunt ut labore et dolore</p><a class="more">READ MORE</a></article>

<section class="newsletter">
  <h2 class="abs section-title" style="top:3880px;font-size:34px">SUBSCRIBE OUR NEWSLETTER</h2>
  <p>Lorem ipsum dolor sit amet, consectetur adipiscing elit, sed do eiusmod tempor incididunt ut labore et dolore magna aliqua. Ut enim ad minim veniam, quis nostrud exercitation ullamco</p>
  <div class="abs subscribe">Enter Your Email Address<a class="btn-pill">Subscribe</a></div>
</section>

<footer class="abs footer">
  <h4 style="left:90px">Main menu</h4>
  <div class="links" style="left:90px">Jewellery<br>Diamonds<br>Engagement<br>Wedding</div>
  <div class="links" style="left:225px">Watches Sale<br>Fashion Jewelry<br>Communion Baptism<br>&nbsp;Blog</div>
  <h4 style="left:410px">Stay In Touch</h4>
  <svg style="position:absolute;left:410px;top:125px" width="120" height="20" viewBox="0 0 120 20"><circle cx="7" cy="10" r="6" fill="#fff"/><rect x="29" y="4" width="12" height="12" fill="#fff"/><circle cx="62" cy="10" r="6" fill="#fff"/><rect x="81" y="4" width="17" height="12" fill="#fff"/><path d="M81 4l8.5 6 8.5-6" stroke="#1b191c" stroke-width="1.5" fill="none"/></svg>
  <h4 style="left:600px">Contact Us</h4>
  <div class="links" style="left:600px;font-size:11px;line-height:27px">412 ORCHARD LN #3 FAIRVIEW,<br>CA 90210 LOS ANGELES<br><span style="color:var(--accent)">■</span> 555 0142 0198<br><span style="color:var(--accent)">■</span> INFO@VELMOR.EXAMPLE</div>
  <h4 style="left:826px">News &amp; updates</h4>
  <div class="field">Enter Your Email address</div>
  <div class="signup">Sign Up</div>
  <div class="copy">© Copyrights.2021.The Company Name.All Rights Reserved</div>
  <div class="cards"><span></span><span></span><span></span><span></span></div>
</footer>

</body>
</html>
```